Business Card Design Project

Basic business card with minimal details. I just need company name, email & web address, telephone and my name.
I would like the back of the card to be grey with my logo & company name centred.

Target Market(s)

Architects
Builders
Property Developers

Industry/Entity Type

Business

Font styles to use
Sans Serif

Colors

Designer to choose colors to be used in the design.

Requirements
Must have
• Framewise Build
Marcus Helby - Director
M: 0427 593184
E: marcus@framewisebuild.com.au
W: www.framewisebuild.com.au
Should not have
• No other images or pictures

```html
<!DOCTYPE html>
<html lang="en">
<head>
<meta charset="utf-8">
<title>Framewise Build — Business Cards</title>
<link rel="stylesheet" href="https://fonts.googleapis.com/css2?family=Exo+2:wght@500;600&family=Open+Sans:wght@400&display=swap">
<style>
  :root {
    --slate: #4b5d6b;
    --crimson: #b0123a;
    --paper: #ffffff;
    --backdrop: #d9dadc;
    --ink-light: #f2f4f6;
    --shadow: rgba(0, 0, 0, 0.28);
  }
  * { box-sizing: border-box; margin: 0; padding: 0; }
  html, body {
    width: 1200px;
    height: 1000px;
    overflow: hidden;
    background: var(--backdrop);
  }
  .sheet {
    position: relative;
    width: 1200px;
    height: 1000px;
  }
  .card {
    position: absolute;
    width: 520px;
    height: 260px;
    box-shadow: 0 4px 10px var(--shadow);
  }
  .card--slate { background: var(--slate); }
  .card--paper { background: var(--paper); }

  .card--front { left: 260px; top: 70px; }
  .card--back-slate { left: 50px; top: 410px; }
  .card--back-paper { left: 630px; top: 410px; }
  .card--back-mono { left: 340px; top: 710px; }

  .holder {
    position: absolute;
    left: 300px;
    top: 22px;
  }
  .holder__name {
    font-family: "Exo 2", sans-serif;
    font-weight: 600;
    font-size: 19px;
    color: var(--crimson);
    letter-spacing: 0.5px;
  }
  .holder__role {
    font-family: "Open Sans", sans-serif;
    font-size: 11px;
    color: var(--ink-light);
    margin-top: -2px;
  }
  .contact {
    position: absolute;
    left: 300px;
    top: 172px;
    list-style: none;
    font-family: "Open Sans", sans-serif;
    font-size: 13px;
    color: var(--ink-light);
  }
  .contact__item {
    display: flex;
    align-items: center;
    gap: 8px;
    height: 21px;
  }
  .contact__icon { width: 12px; height: 12px; flex: none; }

  .brand {
    position: absolute;
    inset: 0;
    display: flex;
    flex-direction: column;
    align-items: center;
    justify-content: center;
    gap: 26px;
  }
  .brand__square {
    width: 56px;
    height: 56px;
    background: var(--crimson);
  }
  .brand__square--light { background: var(--paper); }
  .brand__name {
    font-family: "Exo 2", sans-serif;
    font-weight: 500;
    font-size: 34px;
    letter-spacing: 2px;
    text-transform: uppercase;
    color: var(--paper);
  }
  .brand__name--dark { color: var(--slate); }
</style>
</head>
<body>
<main class="sheet">

  <section class="card card--slate card--front" aria-label="Card front">
    <div class="holder">
      <p class="holder__name">Marcus Helby</p>
      <p class="holder__role">Director</p>
    </div>
    <ul class="contact">
      <li class="contact__item">
        <svg class="contact__icon" viewBox="0 0 12 12" aria-hidden="true">
          <rect x="3" y="0.5" width="6" height="11" rx="1" fill="none" stroke="#b0123a" stroke-width="1.4"/>
          <rect x="4.5" y="9" width="3" height="1" fill="#b0123a"/>
        </svg>
        <span>0427 593184</span>
      </li>
      <li class="contact__item">
        <svg class="contact__icon" viewBox="0 0 12 12" aria-hidden="true">
          <rect x="0.5" y="2.5" width="11" height="7" fill="#b0123a"/>
          <path d="M0.5 2.5 L6 6.5 L11.5 2.5" fill="none" stroke="#4b5d6b" stroke-width="1"/>
        </svg>
        <span>marcus@framewisebuild.com.au</span>
      </li>
      <li class="contact__item">
        <svg class="contact__icon" viewBox="0 0 12 12" aria-hidden="true">
          <circle cx="6" cy="6" r="5.2" fill="none" stroke="#b0123a" stroke-width="1.3"/>
          <ellipse cx="6" cy="6" rx="2.2" ry="5.2" fill="none" stroke="#b0123a" stroke-width="1"/>
          <line x1="0.8" y1="6" x2="11.2" y2="6" stroke="#b0123a" stroke-width="1"/>
        </svg>
        <span>www.framewisebuild.com.au</span>
      </li>
    </ul>
  </section>

  <section class="card card--slate card--back-slate" aria-label="Card back, slate">
    <div class="brand">
      <div class="brand__square"></div>
      <p class="brand__name">Framewise Build</p>
    </div>
  </section>

  <section class="card card--paper card--back-paper" aria-label="Card back, white">
    <div class="brand">
      <div class="brand__square"></div>
      <p class="brand__name brand__name--dark">Framewise Build</p>
    </div>
  </section>

  <section class="card card--slate card--back-mono" aria-label="Card back, slate mono">
    <div class="brand">
      <div class="brand__square brand__square--light"></div>
      <p class="brand__name">Framewise Build</p>
    </div>
  </section>

</main>
</body>
</html>
```